HTML Email Blast design

We need an HTML email blast designed.
Uploaded files include:
- specs attached in file named kelvora-press eblast specs.
- copy / content - word document
- logo

Here's an example of an eblast I really like:
https://mailpreviewhub.example/84126390-3b2e-4f1a-b962-a7d51c0e93fb2047193856214

-

Industry/Entity Type

Finance

Font styles to use
Sans Serif

```html
<!DOCTYPE html>
<html lang="en">
<head>
<meta charset="utf-8">
<title>Halvern REIT – Structured Finance</title>
<link rel="stylesheet" href="https://fonts.googleapis.com/css2?family=Nunito+Sans:wght@300;400;700;800&display=swap">
<style>
  :root {
    --page-bg: #f0f0f0;
    --sheet-bg: #ffffff;
    --navy: #1f3a7a;
    --ink: #111111;
    --body-text: #555555;
    --strong-text: #333333;
    --hero-top: #2b3350;
    --hero-bottom: #3a3f52;
    --map-blue: #0a86d8;
    --map-grey: #cfcfcf;
    --button-red: #ea5550;
    --footer-bar: #000000;
  }
  * { box-sizing: border-box; margin: 0; padding: 0; }
  html, body {
    width: 887px; height: 1200px; overflow: hidden;
    background: var(--page-bg);
    font-family: "Nunito Sans", Arial, sans-serif;
  }
  .email {
    position: absolute; left: 305px; top: 0;
    width: 277px; height: 1200px;
    background: var(--sheet-bg);
  }
  .block { position: absolute; left: 0; width: 277px; }
  .brand {
    top: 0; height: 75px;
    display: flex; align-items: center; justify-content: center; gap: 6px;
  }
  .brand-mark { width: 14px; height: 14px; background: var(--navy); }
  .brand-name { font-size: 17px; font-weight: 800; color: var(--navy); letter-spacing: 0.3px; }
  .hero {
    top: 75px; height: 185px;
    background: linear-gradient(180deg, var(--hero-top) 0%, #33405e 55%, var(--hero-bottom) 100%);
    display: flex; align-items: center; justify-content: center;
  }
  .hero-title { color: #fff; font-size: 19px; font-weight: 800; }
  .section-title {
    text-align: center; color: var(--ink);
    font-size: 11.3px; font-weight: 400; line-height: 15px;
  }
  .intro-title { top: 279px; font-weight: 700; font-size: 11px; }
  .intro-text {
    top: 302px; padding: 0 14px; text-align: center;
    font-size: 7px; line-height: 12.5px; font-weight: 300; color: var(--body-text);
  }
  .intro-text strong { font-weight: 700; color: var(--strong-text); }
  .list {
    padding: 0 28px; list-style: none;
    font-size: 7px; line-height: 12.5px; font-weight: 400; color: var(--body-text);
    text-align: justify;
  }
  .list li { margin-bottom: 7.5px; }
  .list b { font-weight: 700; color: var(--strong-text); }
  .benefits-title { top: 392px; }
  .benefits-list { top: 431px; }
  .products-title { top: 575px; }
  .products-list { top: 598px; }
  .deal-title { top: 709px; }
  .deal-list { top: 732px; text-align: left; }
  .about-title { top: 876px; }
  .about-stats {
    top: 900px; text-align: center;
    font-size: 7px; font-weight: 700; color: var(--strong-text);
  }
  .portfolio-map {
    position: absolute; left: 8px; top: 934px; width: 260px; height: 161px;
    background: radial-gradient(ellipse at 45% 55%, var(--map-blue) 0%, #4ba3de 55%, var(--map-grey) 100%);
    border-radius: 40px 30px 60px 50px;
  }
  .cta {
    position: absolute; left: 97px; top: 1125px; width: 70px; height: 17px;
    background: var(--button-red); border-radius: 2px;
    color: #fff; font-size: 7px; font-weight: 700;
    display: flex; align-items: center; justify-content: center;
    text-decoration: none;
  }
  .footer-bar { top: 1188px; height: 12px; background: var(--footer-bar); }
</style>
</head>
<body>
  <main class="email">
    <header class="block brand">
      <span class="brand-mark"></span>
      <span class="brand-name">Halvern REIT</span>
    </header>

    <section class="block hero" role="img" aria-label="Senior living dining room with chandeliers, wooden tables and navy cabinetry">
      <h1 class="hero-title">Contact Us!</h1>
    </section>

    <h2 class="block section-title intro-title">Need Financing? We’ve got it.</h2>
    <p class="block intro-text">
      Challenging times demand adaptive measures. We’re constantly thinking outside of the REIT box to develop creative financing solutions. Of course, we continue to offer our core NNN and JV structures. <strong>But, did you know we also offer a variety of structured finance products?</strong> These solutions provide a range of levers Halvern can pull to help finance projects.
    </p>

    <h2 class="block section-title benefits-title">BENEFITS OF STRUCTURED<br>FINANCE:</h2>
    <ol class="block list benefits-list">
      <li><b>1.</b> Provide liquidity through releasing “trapped” equity in properties</li>
      <li><b>2.</b> Bridge maturing loans while waiting for the market to return to normal</li>
      <li><b>3.</b> Fund construction for shovel-ready projects</li>
      <li><b>4.</b> Fund existing projects where other investors have backed away</li>
      <li><b>5.</b> Provide an exit plan for equity investors who may have their own liquidity needs</li>
    </ol>

    <h2 class="block section-title products-title">PRODUCTS INCLUDE:</h2>
    <ol class="block list products-list">
      <li><b>1.</b> Preferred Equity</li>
      <li><b>2.</b> Bridge</li>
      <li><b>3.</b> Construction Financing</li>
      <li><b>4.</b> Unitranche Financing</li>
    </ol>

    <h2 class="block section-title deal-title">DEAL PARAMETERS</h2>
    <ul class="block list deal-list">
      <li><b>Transaction Size:</b> $2 - $100 million</li>
      <li><b>Property Types:</b> Independent Living, Assisted Living, Memory Care, Skilled Nursing</li>
      <li><b>Locations:</b> Contiguous US</li>
      <li><b>Financing Types:</b> NNN, JV, Mezzanine, Bridge, Construction, Unitranche, Preferred Equity</li>
      <li><b>Operators:</b> Regional, growth-oriented</li>
    </ul>

    <h2 class="block section-title about-title">ABOUT HALVERN:</h2>
    <p class="block about-stats">180+ Investments | 27 States | 30 Operating Partners</p>
    <div class="portfolio-map" role="img" aria-label="Map of the contiguous United States with the 27 investment states highlighted in blue"></div>

    <a class="cta" href="#">Contact Us Today</a>

    <div class="block footer-bar"></div>
  </main>
</body>
</html>
```